Summit Grading a Masonry LLC business card

My current business card is very plain. it has my logo and contact information. I woud like something that stands out from the rest. please take a look at my website to see about my company.

Compayt Name - Summit Grading And Masonry
Owner - Martin Galloway
Business Address
Business Website - www.summitgradingandmasonry.example
Email - Summitgradingandmasonry@mailbox.example
Phone - 555-214-3867
Fax - 555-630-2719

Target Market(s)

Everyone age tang is 18 - 85

Industry/Entity Type

Business

Contact Information for Business Card

Nice and professional all in one.

Font styles to use
Serif
Other font styles liked:
• Up to you

Requirements
Must have
• All contact info. The design is up to you.
Nice to have
• All the contact info the design is up to you
Should not have
• I don't have any

```html
<!DOCTYPE html>
<html lang="en">
<head>
<meta charset="utf-8">
<title>Summit Grading &amp; Masonry LLC – Business Card</title>
<link href="https://fonts.googleapis.com/css2?family=Ultra&family=Mulish:wght@400;700;800&display=swap" rel="stylesheet">
<style>
  :root{
    --page:#efeae3;
    --charcoal:#262626;
    --charcoal-mid:#4a4a4a;
    --silver:#f4f4f4;
    --silver-deep:#c9c9c9;
    --orange:#f7921e;
    --ink:#2e2e2e;
    --white:#ffffff;
    --badge-slate:#5c6770;
    --badge-grey:#8b9197;
  }
  *{box-sizing:border-box;margin:0;padding:0}
  html,body{width:1039px;height:1200px;overflow:hidden;background:var(--page)}
  .canvas{position:relative;width:1039px;height:1200px}
  .card{position:absolute;left:140px;width:760px;height:450px;overflow:hidden;border:1px solid #d8d8d8}
  .card--front{top:100px}
  .card--back{top:640px}
  .card__art{position:absolute;inset:0;width:100%;height:100%}
  .wordmark{font-family:"Ultra",serif;text-transform:uppercase;letter-spacing:0.5px;line-height:1}
  .card--front .wordmark{position:absolute;left:0;right:0;top:46px;text-align:center;font-size:49px;color:var(--white);-webkit-text-stroke:2px var(--charcoal);paint-order:stroke fill;text-shadow:2px 2px 0 #111}
  .card--front .wordmark .line{display:block;margin-bottom:8px}
  .card--front .wordmark .line--second{padding-left:20px}
  .wordmark small{font-size:0.72em}
  .website{position:absolute;left:0;right:0;top:396px;text-align:center;font-family:"Mulish",sans-serif;font-weight:800;font-size:23px;color:var(--ink)}
  .card--back .wordmark{position:absolute;left:0;right:0;top:40px;text-align:center;font-size:30px;color:#d9d9d9;-webkit-text-stroke:1.4px #3a3a3a;paint-order:stroke fill}
  .person{position:absolute;left:279px;top:106px;font-family:"Mulish",sans-serif;color:var(--ink)}
  .person__name{font-weight:800;font-size:27px}
  .person__role{font-weight:400;font-size:24px;margin-top:4px;color:#3c3c3c}
  .contacts{position:absolute;left:122px;top:256px;list-style:none;font-family:"Mulish",sans-serif;font-weight:800;font-size:21px;color:var(--white)}
  .contacts li{display:flex;align-items:center;height:24px}
  .contacts li+li{margin-top:11px}
  .contacts li.gap{margin-top:20px}
  .contacts svg{width:24px;height:24px;margin-right:8px;flex:none}
</style>
</head>
<body>
<main class="canvas">

  <section class="card card--front" aria-label="Card front">
    <svg class="card__art" viewBox="0 0 760 450" aria-hidden="true">
      <defs>
        <linearGradient id="front-dark" x1="0" y1="0" x2="0" y2="1">
          <stop offset="0" stop-color="#2a2a2a"/>
          <stop offset="0.55" stop-color="#1e1e1e"/>
          <stop offset="1" stop-color="#6a6a6a"/>
        </linearGradient>
        <linearGradient id="front-light" x1="0" y1="0" x2="1" y2="1">
          <stop offset="0" stop-color="#fbfbfb"/>
          <stop offset="0.6" stop-color="#ececec"/>
          <stop offset="1" stop-color="#c8c8c8"/>
        </linearGradient>
      </defs>
      <rect width="760" height="450" fill="url(#front-dark)"/>
      <path d="M0,218 C200,196 470,184 545,212 C595,232 560,328 558,334 C610,288 690,232 760,212 L760,450 L0,450 Z" fill="url(#front-light)"/>
      <path d="M0,218 C200,196 470,184 545,212 C595,232 560,328 558,334 C610,288 690,232 760,212" fill="none" stroke="var(--orange)" stroke-width="5"/>
      <!-- partner badges as plain shapes -->
      <g class="badges">
        <rect x="200" y="290" width="75" height="82" rx="6" fill="var(--badge-slate)"/>
        <rect x="194" y="318" width="87" height="24" fill="var(--orange)"/>
        <circle cx="368" cy="332" r="44" fill="var(--badge-grey)"/>
        <circle cx="368" cy="332" r="34" fill="#eef0f1"/>
        <rect x="330" y="322" width="76" height="20" fill="var(--white)" stroke="var(--badge-slate)" stroke-width="2"/>
        <path d="M453,292 h78 v62 l-39,22 l-39,-22 Z" fill="var(--badge-slate)"/>
        <path d="M459,300 h66 v50 l-33,19 l-33,-19 Z" fill="var(--orange)"/>
      </g>
    </svg>
    <h1 class="wordmark"><span class="line">Summit Grading</span><span class="line line--second">&amp; Masonry <small>LLC</small></span></h1>
    <p class="website">www.summitgradingandmasonry.example</p>
  </section>

  <section class="card card--back" aria-label="Card back">
    <svg class="card__art" viewBox="0 0 760 450" aria-hidden="true">
      <defs>
        <linearGradient id="back-light" x1="0" y1="0" x2="1" y2="1">
          <stop offset="0" stop-color="#d8d8d8"/>
          <stop offset="0.4" stop-color="#f7f7f7"/>
          <stop offset="1" stop-color="#e2e2e2"/>
        </linearGradient>
        <linearGradient id="back-dark" x1="0" y1="0" x2="0" y2="1">
          <stop offset="0" stop-color="#6b6b6b"/>
          <stop offset="0.35" stop-color="#2c2c2c"/>
          <stop offset="1" stop-color="#222"/>
        </linearGradient>
      </defs>
      <rect width="760" height="450" fill="url(#back-light)"/>
      <path d="M0,214 C90,196 180,150 210,88 C188,160 230,200 300,214 C420,232 600,210 760,202 L760,450 L0,450 Z" fill="url(#back-dark)"/>
      <path d="M0,214 C90,196 180,150 210,88 C188,160 230,200 300,214 C420,232 600,210 760,202" fill="none" stroke="var(--orange)" stroke-width="5"/>
    </svg>
    <h2 class="wordmark">Summit Grading &amp; Masonry <small>LLC</small></h2>
    <div class="person">
      <p class="person__name">Martin Galloway</p>
      <p class="person__role">Owner</p>
    </div>
    <ul class="contacts">
      <li><svg viewBox="0 0 24 24"><path d="M6.5 2.5l3 4-2 2.2c1.3 2.7 3.2 4.7 5.8 6l2.2-2 4 3-2 3.8C10 18.8 5 13.6 3.5 5z" fill="var(--orange)"/></svg>555-214-3867</li>
      <li><svg viewBox="0 0 24 24"><rect x="6" y="2" width="12" height="6" fill="var(--orange)"/><rect x="2" y="8" width="20" height="10" rx="2" fill="var(--orange)"/><rect x="6" y="14" width="12" height="8" fill="var(--white)" stroke="var(--orange)" stroke-width="2"/></svg>555-630-2719</li>
      <li class="gap"><svg viewBox="0 0 24 24"><rect x="2" y="5" width="20" height="14" fill="none" stroke="var(--orange)" stroke-width="2"/><path d="M2 5l10 8 10-8" fill="none" stroke="var(--orange)" stroke-width="2"/></svg>Summitgradingandmasonry@mailbox.example</li>
      <li class="gap"><svg viewBox="0 0 24 24"><path d="M12 1a7.5 7.5 0 0 0-7.5 7.5C4.5 14 12 23 12 23s7.5-9 7.5-14.5A7.5 7.5 0 0 0 12 1z" fill="var(--orange)"/><circle cx="12" cy="8.5" r="3" fill="#2a2a2a"/></svg>418 Ridge Ave, Millbrook, NY 12545</li>
    </ul>
  </section>

</main>
</body>
</html>
```